Harrowgate Building Promo Brochure

Design a simple ,visually impactful brochure that will articulate our company experience and services to prospective clients.

We need to project to have the following elements / structure:
1. Company Intro
2. Company Services
3. Experience
4. Contact Info
5. Images

I'd like to use icons and imagery as needed to illustrate services and experience.
This brochure will be emailed, so the final version will need to be compressed.

I've uploaded our Owner Rep Services, which has phasing, and services (within each phase), see attached. This info needs to be cleanly added to a brochure.

The "Why Harrowgate Building Management" doc, copy, needs to be included in the brochure.

Include contact info:
Harrowgate Building Services, LLC
555-318-0472
www.harrowbldteam.example

Target Market(s)

Restaurants and Hospitality Concepts

Font styles to use
Sans Serif

Colors

Designer to choose colors to be used in the design.

Requirements
Must have
• Very easy to read. Clean.
Information and images should be balanced nicely on the page.

use colors of our logo: red, black, grey, white
Should not have
• Very busy text or images.

```html
<!DOCTYPE html>
<html lang="en">
<head>
<meta charset="utf-8">
<title>Harrowgate Building – Promo Brochure</title>
<link rel="stylesheet" href="https://fonts.googleapis.com/css2?family=Open+Sans:ital,wght@0,400;0,600;0,700;1,400;1,600&family=Ubuntu:wght@400;500;700&display=swap">
<style>
:root{
  --red:#c8161d;
  --red-dark:#8e0f14;
  --black:#151515;
  --charcoal:#2b2b2b;
  --grey:#6d6d6d;
  --grey-light:#eeeeee;
  --white:#ffffff;
  --stage:#e6e6e6;
}
*{box-sizing:border-box;margin:0;padding:0}
html,body{width:671px;height:1200px;overflow:hidden}
body{background:var(--stage);font-family:"Open Sans",Arial,sans-serif;color:var(--black);position:relative}
.spread{position:absolute;left:67px;width:524px;height:340px;display:flex;box-shadow:0 2px 6px rgba(0,0,0,.18)}
.spread--cover{top:62px}
.spread--why{top:432px}
.spread--services{top:802px}
.page{position:relative;width:262px;height:340px;overflow:hidden;background:var(--white)}
.abs{position:absolute}
.photo{position:absolute}
.heading{font-family:"Ubuntu",Arial,sans-serif;font-weight:500;letter-spacing:.02em}
.rule{position:absolute;height:1.4px;background:linear-gradient(90deg,var(--black) 0 63%,var(--red) 63% 100%)}
.brand-name{font-family:"Ubuntu",Arial,sans-serif;font-weight:700;color:var(--white);font-size:5.4px;letter-spacing:.02em;white-space:nowrap}
.brand-mark{position:absolute;background:var(--red)}
.web-bar{position:absolute;left:0;top:317px;height:16px;background:linear-gradient(90deg,var(--red-dark),var(--red));clip-path:polygon(0 0,92% 0,100% 100%,0 100%);display:flex;align-items:center;padding-left:12px;gap:4px;color:var(--white);font-family:"Ubuntu",Arial,sans-serif;font-weight:700;font-size:6.6px}
.service-list{position:absolute;font-family:"Ubuntu",Arial,sans-serif;font-weight:500;letter-spacing:.05em;line-height:1.32}

/* cover left */
.cover-back{background:linear-gradient(180deg,#1c1c1c,#2f2f2f 70%,#1a1a1a)}
.cover-back .hero{left:0;top:0;width:262px;height:150px;background:linear-gradient(180deg,#6f8fb6 0,#a8c0d8 30%,#8a6a48 55%,#3e3a36 75%,#5f7a3c 100%);clip-path:polygon(0 0,100% 0,100% 87%,50% 100%,0 87%)}
.cover-back .tagline{left:0;width:262px;top:161px;text-align:center;color:var(--white);font-size:5px}
.thumb{position:absolute;top:177px;width:78px;height:52px}
.cover-back .service-list{left:14px;top:243px;color:var(--white);font-size:7.2px}
.contact{position:absolute;left:14px;color:var(--white);font-size:5.4px;display:flex;align-items:center;gap:5px}
.contact-icon{width:6px;height:6px;border-radius:1px;background:var(--red)}

/* cover front */
.cover-front .band{left:0;top:0;width:262px;height:340px}
.cover-front .service-list{left:10px;top:262px;color:var(--black);font-size:8.6px;font-weight:700}

/* why spread */
.intro-band{left:0;top:0;width:262px;height:97px;background:linear-gradient(90deg,#151515,#3a3a3a 60%,#222)}
.red-strip{position:absolute;left:0;top:97px;width:262px;height:6px;background:linear-gradient(90deg,var(--red-dark),var(--red),var(--red-dark))}
.intro-copy{left:95px;top:39px;width:158px;color:var(--white);font-size:3.5px;line-height:1.3}
.intro-copy p{margin-bottom:3px}
.why-title{position:absolute;left:11px;top:117px;font-size:6.5px}
.feature{position:absolute;left:11px;width:244px;display:flex;gap:5px}
.hex{width:24px;height:27px;flex:none;clip-path:polygon(50% 0,100% 25%,100% 75%,50% 100%,0 75%,0 25%);background:linear-gradient(180deg,var(--red),var(--red-dark));display:flex;align-items:center;justify-content:center}
.feature-title{font-family:"Ubuntu",Arial,sans-serif;font-weight:500;color:var(--red);font-size:5.8px;letter-spacing:.03em}
.feature-lead{font-size:3.9px;line-height:1.3;color:var(--black)}
.feature-more{font-size:3.8px;line-height:1.3;color:var(--grey);margin-top:1px}
.feature-more ul{list-style:none;padding-left:3px}
.purpose{left:131px;top:287px;width:131px;height:53px;background:linear-gradient(180deg,#2a2a2a,#111);padding:14px 10px 0 11px;color:var(--red);font-style:italic;font-size:4.3px;line-height:1.35}
.testimonial{left:0;top:287px;width:262px;height:53px;background:linear-gradient(90deg,#2c2c2c,#121212);color:var(--white)}
.quote-mark{position:absolute;left:14px;top:6px;font-family:Georgia,serif;font-size:38px;color:#8a8a8a;line-height:1}
.testimonial-text{position:absolute;left:47px;top:8px;width:207px;font-style:italic;font-size:3.9px;line-height:1.45}
.testimonial-text b{font-weight:700}

/* services spread */
.services-title{position:absolute;left:11px;top:160px;font-size:6.8px}
.services-sub{position:absolute;left:11px;top:177px;color:var(--red);font-size:4.5px;letter-spacing:.01em}
.service-item{position:absolute;left:14px;display:flex;align-items:center;gap:5px;font-family:"Ubuntu",Arial,sans-serif;font-size:6px;letter-spacing:.05em}
.service-icon{width:15px;height:15px;border-radius:50%;border:1px solid var(--black);display:flex;align-items:center;justify-content:center}
.matrix-title{position:absolute;left:12px;top:26px;font-size:6.3px;font-weight:700;letter-spacing:.01em}
.matrix-side{left:0;top:47px;width:50px;height:286px;background:linear-gradient(180deg,#151515,#3b3b3b 50%,#151515)}
.phase-label{position:absolute;left:6px;color:var(--white);font-family:"Ubuntu",Arial,sans-serif;font-weight:500;font-size:4.2px;letter-spacing:.02em}
.phase-hex{position:absolute;left:34px;width:32px;height:36px}
.matrix-head{position:absolute;left:50px;top:47px;width:203px;height:8px;background:#7a7a7a;color:var(--white);font-size:2.6px;font-weight:700;display:grid;grid-template-columns:67px 48px 48px 40px;align-items:center;text-align:center}
.matrix-head span:first-child{padding-left:17px}
.phase-grid{position:absolute;left:67px;width:186px;display:grid;grid-template-columns:48px 48px 48px 42px;font-size:2.4px;line-height:1.2;color:#222;background:linear-gradient(90deg,#fff 0 144px,#f1f1f1 144px)}
.phase-grid span{padding:0 2px;border-bottom:.3px solid #dddddd;display:flex;align-items:center}
.phase-grid .milestones{grid-column:4;flex-direction:column;justify-content:center;text-align:center;gap:2px;border:none}
</style>
</head>
<body>

<!-- Spread 1: covers -->
<section class="spread spread--cover">
  <article class="page cover-back">
    <div class="photo hero" role="img" aria-label="Photo of a timber-framed restaurant building with landscaped lawn under a blue sky"></div>
    <svg class="abs" style="left:0;top:129px" width="262" height="22" viewBox="0 0 262 22"><polyline points="0,1.5 131,20.5 262,1.5" fill="none" stroke="#fff" stroke-width="1.4"/></svg>
    <p class="abs tagline">GENERAL CONSTRUCTION + PROGRAM MANAGEMENT + DESIGN + OWNER REP</p>
    <div class="thumb" style="left:10px;background:linear-gradient(180deg,#9fb7cf,#4a4a4a 55%,#b0211f 80%,#6b6b6b)" role="img" aria-label="Restaurant exterior with red facade at dusk"></div>
    <div class="thumb" style="left:92px;background:linear-gradient(180deg,#e2d7c6,#b3876a 55%,#7a5a44)" role="img" aria-label="Restaurant frontage with rooftop lettering"></div>
    <div class="thumb" style="left:174px;background:linear-gradient(135deg,#f0b040,#d9581c 45%,#7a3a1c)" role="img" aria-label="Warm-lit restaurant dining interior"></div>
    <div class="service-list">DESIGN<br>PROGRAM MANAGEMENT<br>PROJECT MANAGEMENT<br>CONSTRUCTION MANAGEMENT</div>
    <div class="contact" style="top:284px"><span class="contact-icon"></span>555-318-0472</div>
    <div class="contact" style="top:295px"><span class="contact-icon"></span>dana@harrowbldteam.example</div>
    <div class="contact" style="top:305px"><span class="contact-icon"></span>www.harrowbldteam.example</div>
    <div class="web-bar" style="width:176px"><svg width="6" height="6" viewBox="0 0 12 12"><circle cx="6" cy="6" r="5" fill="none" stroke="#fff" stroke-width="1.2"/><path d="M1 6h10M6 1c-3 3-3 7 0 10M6 1c3 3 3 7 0 10" fill="none" stroke="#fff" stroke-width="1"/></svg>www.harrowbldteam.example</div>
    <span class="brand-mark" style="left:202px;top:272px;width:20px;height:20px"></span>
    <span class="abs brand-name" style="left:187px;top:320px">HARROWGATE BUILDING</span>
  </article>

  <article class="page cover-front">
    <div class="photo band" role="img" aria-label="Evening aerial view of an outdoor dining and entertainment park with string lights"
         style="background:linear-gradient(160deg,#8b7fa8 0,#3b4a5a 25%,#1f2a26 45%,#5a3a22 60%,#2a3230 80%,#1c2228 100%);clip-path:polygon(0 0,18px 0,262px 140px,262px 340px,224px 340px,0 195px)"></div>
    <svg class="abs" style="left:0;top:0" width="262" height="340" viewBox="0 0 262 340">
      <line x1="14" y1="-2" x2="190" y2="102" stroke="#111" stroke-width="5"/>
      <line x1="0" y1="193" x2="190" y2="303" stroke="#111" stroke-width="5"/>
    </svg>
    <span class="brand-mark" style="left:200px;top:20px;width:24px;height:24px"></span>
    <span class="abs brand-name" style="left:178px;top:72px;color:var(--black);font-size:6px">HARROWGATE BUILDING</span>
    <div class="service-list">DESIGN<br>PROGRAM MANAGEMENT<br>PROJECT MANAGEMENT<br>CONSTRUCTION MANAGEMENT</div>
    <div class="web-bar" style="width:177px"><svg width="6" height="6" viewBox="0 0 12 12"><circle cx="6" cy="6" r="5" fill="none" stroke="#fff" stroke-width="1.2"/><path d="M1 6h10M6 1c-3 3-3 7 0 10M6 1c3 3 3 7 0 10" fill="none" stroke="#fff" stroke-width="1"/></svg>www.harrowbldteam.example</div>
  </article>
</section>

<!-- Spread 2: why -->
<section class="spread spread--why">
  <article class="page">
    <div class="photo intro-band" role="img" aria-label="Dark toned photo of a site supervisor"></div>
    <span class="brand-mark" style="left:30px;top:20px;width:26px;height:26px"></span>
    <span class="abs brand-name" style="left:12px;top:75px;font-size:5.6px">HARROWGATE BUILDING</span>
    <div class="abs intro-copy">
      <p>Harrowgate Building Services, LLC is a group of Dynamic Professionals with deep histories of managing significant projects inside of the Restaurant, Retail and Entertainment space.</p>
      <p>Competitive Advantage: An intimate knowledge and proven track record of managing Design, Procurement, Architectural, and Construction efforts simultaneously to produce Undeniable Results</p>
      <p>Extensive Network of Qualified Subcontractor Trades &amp; Vendors</p>
    </div>
    <div class="red-strip"></div>
    <h2 class="heading why-title">WHY HARROWGATE BUILDING MANAGEMENT?</h2>
    <div class="rule" style="left:11px;top:127px;width:150px"></div>

    <div class="feature" style="top:140px">
      <div class="hex"><svg width="12" height="10" viewBox="0 0 12 10"><rect x="1" y="6" width="2" height="4" fill="#fff"/><rect x="4.5" y="4" width="2" height="6" fill="#fff"/><rect x="8" y="2" width="2" height="8" fill="#fff"/><path d="M1 4 6 1l4 0" stroke="#fff" stroke-width=".8" fill="none"/></svg></div>
      <div>
        <h3 class="feature-title">COST SAVINGS</h3>
        <p class="feature-lead">If your concepts' annual project volume is between (1–15) projects, you could save money outsourcing, vs utilizing in-house CM's or PM's.</p>
        <p class="feature-more">Why? When you compare the compensation package w/ all benefits of a qualified Project Manager with 5+ year of management experience, the per-project cost burden from Harrowgate, is potentially 20-30 % less.</p>
      </div>
    </div>
    <div class="feature" style="top:186px">
      <div class="hex"><svg width="12" height="12" viewBox="0 0 12 12"><circle cx="7" cy="7" r="4" fill="none" stroke="#fff" stroke-width="1"/><path d="M7 7V4.5M6 1.5h2M0 5h2M0 7h2M0 9h2" stroke="#fff" stroke-width=".9"/></svg></div>
      <div>
        <h3 class="feature-title">SPEED</h3>
        <p class="feature-lead">Most likely, we are going to have much more robust processes and systems in place managing multiple projects simultaneously, at a more dynamic pace.</p>
        <p class="feature-more">Benefit to You? Projects will move through the life cycle more quickly, efficiently and successfully, with guaranteed outcomes.</p>
      </div>
    </div>

    <div class="photo" style="left:0;top:228px;width:131px;height:112px;background:linear-gradient(135deg,#2a2a2a,#4a4a4a 40%,#c87a2a 60%,#3a3a3a);clip-path:polygon(0 28%,60% 0,100% 22%,100% 100%,0 100%)" role="img" aria-label="Worker grinding metal with sparks flying"></div>
    <p class="abs purpose">"Our Purpose is to create High Level Experiences for our clients through Design, Planning, Construction and Development."</p>
  </article>

  <article class="page">
    <div class="photo" style="left:0;top:0;width:262px;height:97px;background:linear-gradient(180deg,#c9d2da,#9aa0a0 45%,#8a7a62 75%,#6a5a48)" role="img" aria-label="Three crew members in hard hats and safety vests overlooking a construction site"></div>
    <div class="red-strip"></div>
    <h2 class="heading why-title" style="left:10px">WHY HARROWGATE BUILDING MANAGEMENT?</h2>
    <div class="rule" style="left:10px;top:127px;width:150px"></div>

    <div class="feature" style="left:10px;top:141px">
      <div class="hex"><svg width="11" height="12" viewBox="0 0 11 12"><path d="M5.5 1 10 3v3.5c0 2.5-2 4.2-4.5 5C3 10.7 1 9 1 6.5V3z" fill="#fff"/></svg></div>
      <div>
        <h3 class="feature-title">INTEGRITY</h3>
        <p class="feature-lead">Because we are outsourced, we will push information faster, and communicate at a much higher level than an internal resource.</p>
        <p class="feature-more">Why? Our value add, is your piece of mind and delivering results. We have a long term vision and strategy, and we are only as good as our last project. We have to keep delivering, while maintaining a high level experience to our customers so that we can thrive and grow.</p>
      </div>
    </div>
    <div class="feature" style="left:10px;top:186px">
      <div class="hex"><svg width="12" height="10" viewBox="0 0 12 10"><rect x="1.5" y="1" width="9" height="6" rx=".5" fill="none" stroke="#fff" stroke-width="1"/><rect x="0" y="8" width="12" height="1.4" fill="#fff"/></svg></div>
      <div>
        <h3 class="feature-title">TECHNOLOGY</h3>
        <p class="feature-lead">We utilize the latest project management software platforms to ensure high level collaboration, accountability and information transfer.</p>
        <div class="feature-more"><ul><li>• SiteLedger</li><li>• TaskSheet</li></ul></div>
      </div>
    </div>
    <div class="feature" style="left:10px;top:231px">
      <div class="hex"><svg width="12" height="10" viewBox="0 0 12 10"><rect x="0" y="2" width="12" height="3" fill="#fff"/><path d="M2 5v5M10 5v5" stroke="#fff" stroke-width="1.2"/><path d="M2 2 4.5 5M6 2l2.5 3" stroke="#c8161d" stroke-width="1"/></svg></div>
      <div>
        <h3 class="feature-title">EXPERIENCE</h3>
        <p class="feature-lead">Put simply, our team has managed hundreds of projects from restaurant, retail, commercial, warehouse, and government / military logistics - nationwide, and overseas.</p>
        <p class="feature-more">What does this mean to you? You get the benefit of "best practices" we've acquired from partnering with other industry leading concepts and organizations.</p>
      </div>
    </div>

    <div class="abs testimonial">
      <span class="quote-mark">&ldquo;</span>
      <p class="testimonial-text">'We've worked with Dana on a number of projects and she consistently commits to the architectural vision and it shows in the end product. While being proactive, she is always quick to respond and does not miss the finer details. I trust her and her team as they are excellent team players while problem-solving as issues arise."<br><b>- Lewis Carran, Owner, Carran Interiors Studio</b></p>
    </div>
  </article>
</section>

<!-- Spread 3: services + matrix -->
<section class="spread spread--services">
  <article class="page">
    <div class="photo" style="left:0;top:0;width:262px;height:157px;background:#111;clip-path:polygon(0 0,100% 0,100% 82%,50% 100%,0 86%)"></div>
    <div class="photo" style="left:0;top:0;width:262px;height:152px;background:linear-gradient(180deg,#1a2a4a 0,#2c3c5e 30%,#c9cdd6 55%,#a02020 70%,#3a3a44 100%);clip-path:polygon(0 0,100% 0,100% 81%,50% 97%,0 85%)" role="img" aria-label="Night view of a restaurant patio with an angular red steel canopy and rooftop lettering"></div>
    <h2 class="heading services-title">SERVICES</h2>
    <div class="rule" style="left:11px;top:169px;width:150px"></div>
    <p class="services-sub">GENERAL CONSTRUCTION + PROGRAM MANAGEMENT + DESIGN + OWNER REP</p>

    <div class="service-item" style="top:190px"><span class="service-icon"><svg width="8" height="8" viewBox="0 0 8 8"><path d="M1 1l6 6M7 1 1 7" stroke="#151515" stroke-width="1.5"/></svg></span>PROJECT MANAGEMENT</div>
    <div class="service-item" style="top:209px"><span class="service-icon"><svg width="8" height="8" viewBox="0 0 8 8"><rect x="1" y="1" width="6" height="6" fill="none" stroke="#151515" stroke-width="1"/><path d="M2.5 3h3M2.5 5h3" stroke="#c8161d" stroke-width=".9"/></svg></span>PROGRAM MANAGEMENT</div>
    <div class="service-item" style="top:228px"><span class="service-icon"><svg width="8" height="8" viewBox="0 0 8 8"><path d="M1 7V3l3-2 3 2v4z" fill="none" stroke="#151515" stroke-width="1"/><rect x="3" y="4.5" width="2" height="2.5" fill="#c8161d"/></svg></span>OWNER REPRESENTATION</div>
    <div class="service-item" style="top:248px"><span class="service-icon"><svg width="8" height="8" viewBox="0 0 8 8"><path d="M1 5a3 3 0 0 1 6 0z" fill="#151515"/><rect x="0.5" y="5" width="7" height="1.2" fill="#c8161d"/></svg></span>CONSTRUCTION MANAGEMENT</div>
    <div class="service-item" style="top:267px"><span class="service-icon"><svg width="8" height="8" viewBox="0 0 8 8"><rect x="0.5" y="2" width="7" height="2.2" fill="#151515"/><path d="M1.5 4.2V7.5M6.5 4.2V7.5" stroke="#151515" stroke-width="1"/></svg></span>GENERAL CONSTRUCTION</div>

    <div class="thumb" style="left:14px;top:289px;width:72px;height:44px;background:linear-gradient(135deg,#b01c1c,#e24a3a 40%,#3a3a3a 75%,#6a6a6a)" role="img" aria-label="Dining room with red feature wall"></div>
    <div class="thumb" style="left:92px;top:289px;width:72px;height:44px;background:linear-gradient(135deg,#f2b94a,#d96a1e 45%,#7a3418)" role="img" aria-label="Restaurant interior with geometric timber ceiling"></div>
    <div class="thumb" style="left:170px;top:289px;width:72px;height:44px;background:linear-gradient(135deg,#3a2a2a,#c22a2a 45%,#e8d0a0 70%,#5a3a2a)" role="img" aria-label="Bar interior with red neon wall lettering"></div>
  </article>

  <article class="page">
    <h2 class="heading matrix-title">OWNER REPRESENTATIVE + CONSTRUCTION MANAGEMENT MATRIX</h2>
    <div class="rule" style="left:12px;top:35px;width:150px"></div>

    <div class="abs matrix-side"></div>
    <div class="matrix-head"><span>SERVICE</span><span>ACTION+DELIVERABLE</span><span>FUEL TO ACTION | VALUE</span><span>MILESTONES</span></div>

    <span class="phase-label" style="top:61px">PLANNING</span>
    <span class="phase-label" style="top:131px">PRECONSTRUCTION</span>
    <span class="phase-label" style="top:210px">CONSTRUCTION</span>

    <div class="phase-grid" style="top:57px;grid-template-rows:repeat(5,13px)">
      <span class="milestones" style="grid-row:1/span 5"><b style="font-weight:400">Determine Project Go Forward</b><b style="font-weight:400">Articulate Project Goals</b><b style="font-weight:400">Full A&amp;E Team Engaged</b></span>
      <span>Site Evaluation</span><span>Site Characteristics Report</span><span>Early Identification of Red Flags</span>
      <span>Project Scope Development</span><span>Project Plan + Scope</span><span>Detailed Plan with Milestones</span>
      <span>Architect / Engineer Selection</span><span>Design Team Interviews</span><span>Alignment on Energy + Personality</span>
      <span>Conceptual Budgeting</span><span>Conceptual Budget</span><span>Historical Data + Vendor Feedback</span>
      <span>Consultant Management</span><span>Assist in Building Team</span><span>Align with Project Schedule</span>
    </div>

    <div class="phase-grid" style="top:129px;grid-template-rows:repeat(6,12px)">
      <span class="milestones" style="grid-row:1/span 6"><b style="font-weight:400">Approved Budget</b><b style="font-weight:400">Approved Schedule</b><b style="font-weight:400">Approved Permit</b><b style="font-weight:400">Procurement Plan in Place</b><b style="font-weight:400">Construction Team in Place</b><b style="font-weight:400">Scope 95% Defined</b></span>
      <span>Consultant Management</span><span>Facilitate Meetings, Notes</span><span>Collaborate + Remove Obstacles</span>
      <span>Budgeting</span><span>Organized Working Budget</span><span>Comprehensive &amp; Transparent</span>
      <span>Procurement &amp; Supplier Management</span><span>Procurement Log, Pricing</span><span>Align with Project Schedule</span>
      <span>Value Engineering</span><span>Get Creative, Stay Aligned</span><span>With Project Goals</span>
      <span>Critical Path Scheduling</span><span>Global Schedule Development</span><span>Comprehensive &amp; Transparent</span>
      <span>GC Bidding &amp; Selection</span><span>GC Comparison, Bid Qualification</span><span>Check References, Philosophy</span>
    </div>

    <div class="phase-grid" style="top:205px;grid-template-rows:repeat(9,14px)">
      <span class="milestones" style="grid-row:1/span 9"><b style="font-weight:400">Safety Goals</b><b style="font-weight:400">Schedule CPM Milestones</b><b style="font-weight:400">Budget Tracking</b><b style="font-weight:400">Completion Date</b><b style="font-weight:400">Successful Turnover</b></span>
      <span>PreConstruction Meetings</span><span>PreCon Meeting Coord</span><span>Collaborate + Apply Pressure</span>
      <span>Scope Review</span><span>Ensure Completeness</span><span>Hold Teams Accountable</span>
      <span>CP Schedule Management</span><span>Weekly Progress Meetings</span><span>Track Meeting Notes</span>
      <span>Project Reporting</span><span>Daily, Weekly Reports</span><span>Identify Progress, Risk</span>
      <span>Document Management</span><span>Drawings, RFIs, Submittals</span><span>High Level of Capture</span>
      <span>Site Visits</span><span>Site Reports, Photographs</span><span>Ensure Quality Met</span>
      <span>Pay App Review</span><span>Determine Pay App Accuracy</span><span>Recommendation by % Complete</span>
      <span>RFI Management</span><span>Maintain RFI Log</span><span>Ensure Distribution</span>
      <span>Punchlist</span><span>Compile, Distribute, Hold</span><span>Pressure to Complete</span>
    </div>

    <div class="phase-hex hex" style="top:76px;width:32px;height:36px"><svg width="14" height="12" viewBox="0 0 14 12"><rect x="2" y="1" width="10" height="7" rx=".6" fill="none" stroke="#fff" stroke-width="1.1"/><rect x="0" y="9.5" width="14" height="1.6" fill="#fff"/></svg></div>
    <div class="phase-hex hex" style="top:143px;width:32px;height:36px"><svg width="14" height="12" viewBox="0 0 14 12"><path d="M2 8a5 5 0 0 1 10 0z" fill="#fff"/><rect x="1" y="8" width="12" height="1.8" fill="#fff"/></svg></div>
    <div class="phase-hex hex" style="top:222px;width:32px;height:36px"><svg width="14" height="12" viewBox="0 0 14 12"><rect x="0" y="2" width="14" height="3.5" fill="#fff"/><path d="M2.5 5.5V12M11.5 5.5V12" stroke="#fff" stroke-width="1.4"/><path d="M2.5 2 5.5 5.5M7 2l3 3.5" stroke="#c8161d" stroke-width="1.1"/></svg></div>
  </article>
</section>

</body>
</html>
```